B2B EDM Banner Design- Specialist Tech Company

We need a new top-of-email banner for our EDM campaigns for Brelmont Digest (www.brelmontdigest.example
). This banner will sit at the top of every email and must immediately signal the brand, look modern and professional, and be visually aligned with the tech/IT audience.
Size of the banner: Around 728x90 - it must fit at the top of an email blast.
Purpose of the Banner
Establish a strong, recognizable brand identity across all Brelmont Digest EDMs
visually consistent with existing banners created for other brands (see reference examples provided)
Communicate Brelmont Digest’s value proposition at a glance
Brand Name
Brelmont Digest
Tagline (must appear in the banner)
“11,322 whitepapers from 726 companies”
Design Requirements
Style & Tone
Modern, clean, and professional
Tech-centric look and feel
High-quality, sleek, and corporate
Eye-catching but not cluttered
Should feel premium and authoritative
Layout & Composition
Full-width banner for email header
Horizontal orientation similar to the StaffLoom and Workforce Paper Vault examples
Include space for the brand name/logo prominently on the left or centered
Integrate the tagline in a readable, secondary position
Optional: a subtle background texture or tech-related abstract pattern (circuitry, network nodes, gradient, etc.)
No busy imagery—should feel clean and trustworthy
Color Palette
Use colors consistent with Brelmont Digest branding from www.brelmontdigest.example
Blues, greys, blacks, and tech-style gradients preferred
Should feel consistent with a B2B IT audience
Typography
Clean, sans-serif fonts (professional/tech-aligned)
Brand name should be bold and prominent
Tagline should be smaller, but still readable on desktop and mobile
Imagery (if used)
Abstract tech shapes, network visuals, geometric patterns, or gradient overlays
Avoid photography of people
Keep imagery subtle so text remains legible
Call-to-Action Button (optional)
None required in this banner (unlike the HR examples)
Banner should remain a pure brand header
Deliverables
Final banner in PNG and JPG formats
2–3 design variations (if possible) for A/B testing
Dimensions optimized for EDM: ~600–700px wide (standard email width), proportionate height

```html
<!DOCTYPE html>
<html lang="en">
<head>
<meta charset="utf-8">
<title>Brelmont Digest – EDM Header Banner</title>
<link href="https://fonts.googleapis.com/css2?family=Roboto:wght@400;700;900&display=swap" rel="stylesheet">
<style>
  :root {
    --stage-grey: #c4c4c4;
    --navy-deep: #0b2c52;
    --navy-mid: #0a4f86;
    --navy-night: #061a30;
    --banner-edge: #ffffff;
    --text-white: #ffffff;
    --accent-cyan: #2aa8e6;
    --particle-glow: rgba(42, 168, 230, 0.35);
  }

  html, body {
    margin: 0;
    padding: 0;
    width: 1200px;
    height: 441px;
    overflow: hidden;
    background: var(--stage-grey);
    font-family: "Roboto", Arial, sans-serif;
  }

  .banner {
    position: absolute;
    left: 88px;
    top: 70px;
    width: 1024px;
    height: 295px;
    box-sizing: border-box;
    border: 2px solid var(--banner-edge);
    background: linear-gradient(90deg,
      var(--navy-deep) 0%,
      #0d4272 25%,
      var(--navy-mid) 42%,
      #08345e 60%,
      var(--navy-night) 100%);
    box-shadow: 0 4px 10px rgba(0, 0, 0, 0.35);
    overflow: hidden;
  }

  .network-visual {
    position: absolute;
    right: 0;
    top: 0;
    width: 560px;
    height: 100%;
    background:
      radial-gradient(ellipse 55% 60% at 70% 50%, var(--particle-glow), transparent 70%),
      radial-gradient(ellipse 40% 80% at 95% 40%, rgba(42, 168, 230, 0.2), transparent 75%);
  }

  .brand {
    position: absolute;
    left: 73px;
    top: 80px;
    display: flex;
    align-items: center;
    gap: 14px;
  }

  .brand-mark {
    width: 52px;
    height: 52px;
    background: var(--accent-cyan);
  }

  .brand-name {
    margin: 0;
    font-size: 36px;
    font-weight: 700;
    line-height: 1;
    letter-spacing: 0.5px;
    color: var(--text-white);
    text-transform: uppercase;
  }

  .brand-subline {
    margin: 6px 0 0;
    font-size: 12px;
    font-weight: 700;
    letter-spacing: 4.2px;
    color: var(--text-white);
    text-transform: uppercase;
  }

  .tagline {
    position: absolute;
    left: 73px;
    top: 160px;
    margin: 0;
    font-size: 34px;
    font-weight: 400;
    color: var(--text-white);
    white-space: nowrap;
  }

  .tagline strong {
    font-size: 44px;
    font-weight: 900;
  }
</style>
</head>
<body>
  <section class="banner">
    <div class="network-visual" role="img" aria-label="Abstract flowing streams of glowing blue network particles"></div>

    <div class="brand">
      <div class="brand-mark"></div>
      <div class="brand-text">
        <h1 class="brand-name">Brelmont Digest</h1>
        <p class="brand-subline">For IT Professionals</p>
      </div>
    </div>

    <p class="tagline"><strong>11,322</strong> whitepapers from <strong>726</strong> companies</p>
  </section>
</body>
</html>
```